Motor Vault Website - Part of the Brantley Group

A complimentary website is required for the launch of a 'Motor Vault' - a new service launched by industry renowned BRANTLEY. Motor Vault is an industry-first brand that designs and builds unique subterranean car parks for private residential homes in London and the influential counties within the UK. Please see here the direction of a new BRANTLEY Website - we would like Motor Vault to be complimentary and sit alongside BRANTLEY harmoniously - https://www.brantleyhq.example/brantley-nu-staging Brantley have some images, but whilst more professional images are in production - we have also attached pixmoor photos- named clearly as pixmoor. **Attached files include JPEG, .eps of logo and Brantley library images and Pixmoor Library Images - two versions of logo dependent on background colour. - Website needs to be sleek, chic and masculine.- Colour Palette - Grey/ Black/ White - Same visiual journey as Brantley website- Required areas within the sit include - About Us / Our Work / Contact Page

Target Market(s)

Luxury
Men

Number of Pages Required

2 page

Font styles to use
Sans Serif

Colors
e8e8e8
757575
1b1b1b
000000
9d9d9d
cbcbcb
f5f5f5

Requirements
Must have
• Complimentary of this site - https://www.brantleyhq.example/brantley-nu-staging
Should not have
• Colour

```html
<!DOCTYPE html>
<html lang="en">
<head>
<meta charset="utf-8">
<title>Motor Vault</title>
<link rel="stylesheet" href="https://fonts.googleapis.com/css2?family=Libre+Baskerville:wght@400;700&family=Work+Sans:wght@300;400;500;600&display=swap">
<style>
:root{
  --black:#000000;
  --ink:#1b1b1b;
  --grey-dark:#757575;
  --grey-mid:#9d9d9d;
  --grey-light:#cbcbcb;
  --field:#e8e8e8;
  --paper:#f5f5f5;
  --white:#ffffff;
  --serif:'Libre Baskerville', Georgia, serif;
  --sans:'Work Sans', Arial, sans-serif;
}
*{margin:0;padding:0;box-sizing:border-box}
h1,h2,h3{font-weight:400}
html,body{width:1200px;height:2821px;overflow:hidden;background:var(--white);font-family:var(--sans);color:var(--ink)}
.page{position:relative;width:1200px;height:2821px}
.abs{position:absolute}

/* hero */
.hero{left:0;top:0;width:1200px;height:640px;background:linear-gradient(180deg,#2b2b2b 0%,#4a4a4a 35%,#3a3a3a 65%,#1e1e1e 100%)}
.brand{position:absolute;display:flex;align-items:center;gap:12px;font-family:var(--sans);font-weight:600;letter-spacing:1px;color:var(--white);white-space:nowrap}
.brand-mark{width:22px;height:22px;background:var(--white)}
.hero .brand{left:87px;top:28px;font-size:32px}
.nav{position:absolute;right:87px;top:43px;display:flex;gap:38px;list-style:none}
.nav li{font-size:13px;letter-spacing:2.5px;color:var(--grey-light)}
.nav li.active{color:var(--white);font-weight:600;border-bottom:1px solid var(--white);padding-bottom:3px}
.hero-rule{position:absolute;left:527px;width:146px;height:2px;background:var(--white)}
.hero-title{position:absolute;left:0;width:1200px;top:305px;text-align:center;font-family:var(--serif);font-size:44px;line-height:54px;letter-spacing:3px;color:var(--white)}
.notch{position:absolute;left:545px;top:606px}

/* welcome */
.welcome-title{left:87px;top:766px;width:590px;white-space:nowrap;font-family:var(--serif);font-size:29px;letter-spacing:1.5px;color:var(--ink)}
.welcome-title b{font-weight:700}
.rule{height:2px;background:var(--grey-light)}
.welcome-text{left:87px;top:846px;width:560px;font-size:13.5px;line-height:24px;color:var(--ink)}
.btn-outline{border:2px solid var(--grey-light);background:var(--white);font-family:var(--sans);font-size:11px;letter-spacing:3px;color:var(--grey-mid);display:flex;align-items:center;justify-content:center}
.welcome-photo{left:701px;top:730px;width:413px;height:350px;background:radial-gradient(ellipse at 55% 55%,#d6d6d6 0%,#7b7b7b 22%,#3a3a3a 55%,#1a1a1a 100%)}

/* work */
.work-band{left:0;top:1166px;width:1200px;height:273px;background:linear-gradient(90deg,#1a1a1a 0%,#3d3d3d 35%,#2a2a2a 60%,#444 100%)}
.section-title{left:0;width:1200px;text-align:center;font-family:var(--serif);font-size:33px;letter-spacing:2px}
.work-card{border:4px solid var(--white);background:linear-gradient(160deg,#555 0%,#222 55%,#0c0c0c 100%)}
.work-label{background:var(--white);font-family:var(--serif);font-size:16px;letter-spacing:1.5px;color:var(--ink);display:flex;align-items:center;justify-content:center;white-space:nowrap}

/* statement */
.statement{left:0;top:1715px;width:1200px;height:303px;background:linear-gradient(180deg,#141414 0%,#2a2a2a 50%,#0a0a0a 100%)}
.statement-title{left:0;width:1200px;top:1798px;text-align:center;font-family:var(--serif);font-size:21px;letter-spacing:2px;color:var(--white)}
.statement-text{left:340px;width:520px;top:1866px;text-align:center;font-size:13.5px;line-height:24px;color:var(--grey-light)}

/* contact */
.field{background:var(--paper);border-left:3px solid var(--grey-dark);font-size:12px;color:var(--grey-mid);padding:15px 0 0 16px}
.info{left:771px;font-size:17px;line-height:27px;color:var(--ink);white-space:nowrap}
.info-icon{left:727px}
.social{width:32px;height:32px;background:var(--grey-dark);transform:rotate(45deg);border-radius:3px}

/* footer */
.footer{left:0;top:2577px;width:1200px;height:244px;background:var(--black)}
.footer-brand{left:0;width:1200px;justify-content:center;top:2640px;font-size:36px}
.legal{left:0;width:1200px;text-align:center;font-size:11px;letter-spacing:2px;color:var(--grey-dark);line-height:21px;top:2715px}
</style>
</head>
<body>
<div class="page">

  <header class="abs hero" role="img" aria-label="Black and white photo of workers excavating an underground car park">
    <div class="brand"><span class="brand-mark"></span>MOTOR VAULT</div>
    <ul class="nav">
      <li class="active">HOME</li><li>ABOUT US</li><li>OUR WORK</li><li>CONTACT</li>
    </ul>
    <div class="hero-rule" style="top:288px"></div>
    <h1 class="hero-title">BUILDS UNIQUE<br>SUBTERRANEAN CAR PARKS</h1>
    <div class="hero-rule" style="top:428px"></div>
    <svg class="notch" width="113" height="34" viewBox="0 0 113 34">
      <polygon points="0,34 56.5,0 113,34" fill="#ffffff"/>
      <polyline points="45,12 56.5,22 68,12" fill="none" stroke="#1b1b1b" stroke-width="2"/>
    </svg>
  </header>

  <h2 class="abs welcome-title">WELCOME TO <b>MOTOR VAULT</b></h2>
  <div class="abs rule" style="left:87px;top:824px;width:70px"></div>
  <p class="abs welcome-text">Lorem ipsum dolor sit amet, consectetur adipiscing elit. In iaculis tellus tortor, in lacinia nulla commodo vitae. Aliquam pulvinar eros id ultricies sagittis. Vivamus sodales ligula id pellentesque tempus. Ut scelerisque condimentum pretium. Aenean eu metus sed dui blandit scelerisque. Nam nec pretium metus. Vivamus erat massa, condimentum ac purus ac, egestas volutpat est.</p>
  <div class="abs btn-outline" style="left:87px;top:991px;width:175px;height:46px">READ MORE</div>
  <div class="abs welcome-photo" role="img" aria-label="Black and white photo of a finished concrete underground car park corridor"></div>
  <svg class="abs" style="left:701px;top:730px" width="413" height="350" viewBox="0 0 413 350">
    <polyline points="27,52 27,27 52,27" fill="none" stroke="#ffffff" stroke-width="3"/>
    <polyline points="361,323 386,323 386,298" fill="none" stroke="#ffffff" stroke-width="3"/>
  </svg>

  <div class="abs work-band" role="img" aria-label="Black and white photo of dimpled waterproof membrane on basement walls"></div>
  <h2 class="abs section-title" style="top:1246px;color:var(--white)">OUR WORK</h2>
  <div class="abs work-card" style="left:132px;top:1352px;width:410px;height:270px" role="img" aria-label="Photo of excavation machinery beneath a supported house"></div>
  <div class="abs work-label" style="left:192px;top:1595px;width:290px;height:34px">LOREM IPSUM DUMMY</div>
  <div class="abs work-card" style="left:660px;top:1352px;width:410px;height:270px" role="img" aria-label="Photo of a welder cutting steel props underground with sparks"></div>
  <div class="abs work-label" style="left:718px;top:1595px;width:290px;height:34px">CONTRARY POPULAR</div>

  <section class="abs statement" role="img" aria-label="Dark photo of an underground construction space"></section>
  <h3 class="abs statement-title">LOREM IPSUM IS SIMPLY DUMMY TEXT</h3>
  <div class="abs" style="left:567px;top:1845px;width:66px;height:2px;background:var(--grey-mid)"></div>
  <p class="abs statement-text">Duis ultricies vehicula libero. Integer vitae turpis id diam sollicitudin placerat non sed justo. Sed ut accumsan massa, et consectetur tellus. Maecenas lobortis faucibus venenatis.</p>

  <h2 class="abs section-title" style="top:2088px;color:var(--ink)">CONTACT US</h2>
  <div class="abs rule" style="left:566px;top:2148px;width:68px"></div>
  <div class="abs field" style="left:173px;top:2193px;width:414px;height:46px">Name</div>
  <div class="abs field" style="left:173px;top:2263px;width:414px;height:47px">Email</div>
  <div class="abs field" style="left:173px;top:2334px;width:414px;height:82px">Message</div>
  <div class="abs btn-outline" style="left:173px;top:2441px;width:177px;height:46px">SUBMIT</div>

  <svg class="abs info-icon" style="top:2190px" width="22" height="28" viewBox="0 0 22 28">
    <path d="M11 26 C4 17 2 13 2 10 A9 9 0 0 1 20 10 C20 13 18 17 11 26Z" fill="none" stroke="#1b1b1b" stroke-width="1.8"/>
    <circle cx="11" cy="10" r="3.2" fill="none" stroke="#1b1b1b" stroke-width="1.8"/>
  </svg>
  <p class="abs info" style="top:2186px">48 Harrow Row<br>London<br>W9 2QT</p>
  <svg class="abs info-icon" style="top:2294px" width="24" height="24" viewBox="0 0 24 24">
    <path d="M5 3 L9 3 L10.5 8 L8 10 C9.5 13 11 14.5 14 16 L16 13.5 L21 15 L21 19 C21 20 20 21 19 21 C10 21 3 14 3 5 C3 4 4 3 5 3Z" fill="none" stroke="#1b1b1b" stroke-width="1.6"/>
  </svg>
  <p class="abs info" style="top:2292px">Tel: 0207 946 0123</p>
  <svg class="abs info-icon" style="top:2350px" width="24" height="18" viewBox="0 0 24 18">
    <rect x="1" y="1" width="22" height="16" fill="none" stroke="#1b1b1b" stroke-width="1.6"/>
    <polyline points="1,1 12,10 23,1" fill="none" stroke="#1b1b1b" stroke-width="1.6"/>
  </svg>
  <p class="abs info" style="top:2345px">Email: info@motorvault.example</p>
  <div class="abs social" style="left:736px;top:2421px"></div>
  <div class="abs social" style="left:796px;top:2421px"></div>
  <div class="abs social" style="left:858px;top:2421px"></div>
  <div class="abs social" style="left:920px;top:2421px"></div>

  <footer class="abs footer"></footer>
  <div class="brand footer-brand"><span class="brand-mark"></span>MOTOR VAULT</div>
  <p class="abs legal">COPYRIGHT © MOTORVAULT 2019.<br>TERMS AND CONDITIONS | PRIVACY POLICY</p>

</div>
</body>
</html>
```